SaaS Early tech startup business card design

Unique design for experience ecommerce platform company. the business cards will be used by executive members. conformance with color code is required.

```html
<!DOCTYPE html>
<html lang="en">
<head>
<meta charset="utf-8">
<title>novra — Business Card</title>
<link rel="stylesheet" href="https://fonts.googleapis.com/css2?family=Open+Sans:wght@400;700&display=swap">
<style>
  :root {
    --page-bg: #ffffff;
    --card-light: #ffffff;
    --card-dark: #222135;
    --ink-dark: #1f1f2e;
    --ink-light: #ffffff;
    --brand-teal: #17809a;
    --rule-dark: #3a3c52;
    --rule-light: #ffffff;
    --tone-core: #10b99a;
    --tone-mid: #1a8aab;
    --tone-edge: #0b6591;
    --tone-edge-dark: #1c3c62;
  }
  html, body {
    margin: 0;
    padding: 0;
    width: 1200px;
    height: 1200px;
    overflow: hidden;
    background: var(--page-bg);
    font-family: "Open Sans", Arial, sans-serif;
  }
  .canvas {
    position: relative;
    width: 1200px;
    height: 1200px;
  }
  .card {
    position: absolute;
    top: 469px;
    width: 405px;
    height: 262px;
    overflow: hidden;
    box-shadow: 2px 3px 5px rgba(0, 0, 0, 0.22);
  }
  .card-front { left: 121px; background: var(--card-light); }
  .card-back  { left: 650px; background: var(--card-dark); }
  .accent-disc {
    position: absolute;
    border-radius: 50%;
  }
  .card-front .accent-disc {
    width: 350px;
    height: 350px;
    left: -169px;
    top: -28px;
    background: radial-gradient(circle, var(--tone-core) 0%, var(--tone-mid) 55%, var(--tone-edge) 100%);
  }
  .card-back .accent-disc {
    width: 346px;
    height: 346px;
    left: 232px;
    top: -173px;
    background: radial-gradient(circle, var(--tone-core) 0%, var(--tone-mid) 50%, var(--tone-edge-dark) 100%);
  }
  .brand-name {
    position: absolute;
    margin: 0;
    font-weight: 700;
    font-size: 38px;
    line-height: 1;
    letter-spacing: 0.5px;
    color: var(--brand-teal);
  }
  .card-front .brand-name { right: 50px; top: 40px; }
  .card-back .brand-name { left: 26px; top: 40px; }
  .rule {
    position: absolute;
    height: 1.5px;
  }
  .card-front .rule { left: 233px; width: 121px; top: 81px; background: var(--rule-dark); }
  .card-back .rule { left: 26px; width: 128px; top: 193px; background: var(--rule-light); }
  .tagline {
    position: absolute;
    right: 50px;
    top: 90px;
    margin: 0;
    text-align: right;
    font-size: 14px;
    line-height: 17.8px;
    color: var(--ink-dark);
  }
  .contact-list {
    position: absolute;
    left: 26px;
    top: 200px;
    margin: 0;
    padding: 0;
    list-style: none;
    color: var(--ink-light);
    font-size: 17.2px;
    line-height: 20.5px;
  }
  .contact-list li {
    display: flex;
    align-items: center;
    gap: 7px;
  }
  .contact-list svg { flex: none; }
</style>
</head>
<body>
<main class="canvas">

  <section class="card card-front" aria-label="Business card front">
    <div class="accent-disc" role="img" aria-label="Large teal-to-blue circular decorative motif on the left edge"></div>
    <h1 class="brand-name">novra</h1>
    <div class="rule"></div>
    <p class="tagline">Lorem Ipsum is<br>simply dummy<br>text of the<br>printing and<br>typesetting<br>industry.</p>
  </section>

  <section class="card card-back" aria-label="Business card back">
    <div class="accent-disc" role="img" aria-label="Teal-to-navy circular decorative motif in the top right corner"></div>
    <h2 class="brand-name">novra</h2>
    <div class="rule"></div>
    <ul class="contact-list">
      <li>
        <svg width="13" height="13" viewBox="0 0 13 13" aria-hidden="true">
          <rect x="0.75" y="0.75" width="11.5" height="11.5" rx="2" fill="none" stroke="#fff" stroke-width="1.5"/>
          <rect x="3" y="4" width="7" height="5" fill="none" stroke="#fff" stroke-width="1"/>
          <path d="M3 4 L6.5 7 L10 4" fill="none" stroke="#fff" stroke-width="1"/>
        </svg>
        <span>Lorem Ipsum Lorem Ipsum</span>
      </li>
      <li>
        <svg width="13" height="13" viewBox="0 0 13 13" aria-hidden="true">
          <rect x="0.75" y="0.75" width="11.5" height="11.5" rx="2" fill="none" stroke="#fff" stroke-width="1.5"/>
          <path d="M6.5 10.5 C4.5 8.2 3.8 6.8 3.8 5.6 A2.7 2.7 0 0 1 9.2 5.6 C9.2 6.8 8.5 8.2 6.5 10.5 Z" fill="#fff"/>
          <circle cx="6.5" cy="5.6" r="1" fill="var(--card-dark)"/>
        </svg>
        <span>Lorem Ipsum Lorem Ipsum</span>
      </li>
    </ul>
  </section>

</main>
</body>
</html>
```